IT Company based on Biology Business Needs a Business Card Design

We need a business card design for a new company called 'Lumen CELL'. We develop the machine learning solutions especially focused on deep learning algorithms for biology industry. Our initial product is a vision detection on biological images to help doctors diagnose the symptoms. We would like to see designs that use the color green.

Industry/Entity Type

Business

```html
<!DOCTYPE html>
<html lang="en">
<head>
<meta charset="UTF-8">
<title>Lumen CELL — Business Card</title>
<link href="https://fonts.googleapis.com/css2?family=Arimo:wght@400;700&display=swap" rel="stylesheet">
<style>
  :root {
    --backdrop: #3b3d40;
    --card-white: #ffffff;
    --card-shade: #f1f2f1;
    --brand-green: #6cb33f;
    --brand-green-dark: #4f8f2c;
    --brand-green-light: #8cc63f;
    --text-grey: #555a5e;
    --icon-green: #5aa532;
  }
  * { box-sizing: border-box; margin: 0; padding: 0; }
  html, body {
    width: 1200px; height: 950px; overflow: hidden;
    background: var(--backdrop);
    font-family: "Arimo", Arial, sans-serif;
  }
  .stage {
    width: 1200px; height: 950px;
    display: flex; flex-direction: column;
    align-items: center; justify-content: center; gap: 50px;
  }
  .card {
    position: relative;
    width: 700px; height: 400px;
    border-radius: 4px;
    overflow: hidden;
    box-shadow: 0 10px 24px rgba(0,0,0,0.35);
  }
  /* Front */
  .card-front {
    background: linear-gradient(135deg, var(--card-white) 55%, var(--card-shade));
  }
  .brand {
    position: absolute; left: 60px; top: 70px;
    display: flex; align-items: center; gap: 14px;
  }
  .brand-dot {
    width: 30px; height: 30px; border-radius: 50%;
    background: var(--brand-green);
  }
  .brand-name {
    font-size: 44px; font-weight: 400; letter-spacing: -1px;
    color: var(--brand-green);
  }
  .divider {
    position: absolute; left: 34px; top: 200px; width: 500px; height: 10px;
  }
  .contact-list {
    position: absolute; left: 40px; top: 228px;
    list-style: none;
    font-size: 18px; color: var(--text-grey); line-height: 27px;
  }
  .contact-list li { display: flex; align-items: center; gap: 10px; }
  .contact-list svg { width: 16px; height: 16px; flex: none; }
  .person {
    position: absolute; right: 48px; top: 190px; text-align: right;
  }
  .person-name {
    font-size: 23px; font-weight: 700; color: var(--brand-green);
  }
  .person-role {
    font-size: 18px; font-weight: 700; color: var(--brand-green-dark);
    margin-top: 4px;
  }
  .address {
    position: absolute; right: 48px; bottom: 60px; text-align: right;
    font-size: 19px; color: var(--text-grey); line-height: 27px;
    letter-spacing: 0.5px;
  }
  /* Back */
  .card-back {
    background: linear-gradient(120deg, var(--brand-green-light), var(--brand-green) 50%, var(--brand-green-dark));
    display: flex; align-items: center; justify-content: center; gap: 16px;
  }
  .card-back .brand-dot { background: #ffffff; opacity: 0.9; width: 36px; height: 36px; }
  .card-back .brand-name { color: #ffffff; font-size: 52px; }
</style>
</head>
<body>
<main class="stage">
  <section class="card card-front" aria-label="Business card front">
    <div class="brand">
      <span class="brand-dot"></span>
      <span class="brand-name">Lumen CELL</span>
    </div>

    <svg class="divider" viewBox="0 0 500 10" aria-hidden="true">
      <line x1="5" y1="5" x2="495" y2="5" stroke="var(--brand-green)" stroke-width="1.6"/>
      <circle cx="5" cy="5" r="3.5" fill="var(--brand-green)"/>
      <circle cx="495" cy="5" r="3.5" fill="var(--brand-green)"/>
    </svg>

    <ul class="contact-list">
      <li>
        <svg viewBox="0 0 16 16" aria-hidden="true"><path d="M3 2h3l1.5 3.5-2 1.3a8 8 0 0 0 3.7 3.7l1.3-2L14 10v3a1 1 0 0 1-1 1A11 11 0 0 1 2 3a1 1 0 0 1 1-1z" fill="var(--icon-green)"/></svg>
        555 0142 7781
      </li>
      <li>
        <svg viewBox="0 0 16 16" aria-hidden="true"><rect x="4" y="1" width="8" height="14" rx="1.5" fill="none" stroke="var(--icon-green)" stroke-width="1.8"/><circle cx="8" cy="12.3" r="1" fill="var(--icon-green)"/></svg>
        555 0198 3346
      </li>
      <li>
        <svg viewBox="0 0 16 16" aria-hidden="true"><rect x="1" y="3" width="14" height="10" rx="1" fill="var(--icon-green)"/><path d="M1.5 3.8 8 9l6.5-5.2" fill="none" stroke="#fff" stroke-width="1.2"/></svg>
        mara@example.com
      </li>
    </ul>

    <div class="person">
      <p class="person-name">Mara Quill</p>
      <p class="person-role">President</p>
    </div>

    <address class="address" style="font-style:normal">
      4120 Alder Grove Lane<br>
      Brookline Falls, NY 10482<br>
      www.example.com
    </address>
  </section>

  <section class="card card-back" aria-label="Business card back">
    <span class="brand-dot"></span>
    <span class="brand-name">Lumen CELL</span>
  </section>
</main>
</body>
</html>
```